#1 Selling Sweden weight loss supplement comes to USA - LABEL needed!

The number one weight loss in Sweden is coming to USA

-I need a label that is clean and simple but somehow represents, in an abstract way, weight loss or slender.
-The product and water mixed is all the is needed. This too could be represented in the label design.
-The bottle will be white.

-Attached is a picture of a supplement bottle with
--the logo for the company, 'NuKelvara'
--the name of the supplement, 'Kelvara Lithe'
and
--other text that could be included in the final label.

ALSO attached are 2 label designs that I like. This might give you an idea of a direction to go.
Thank You very much.

Target Market(s)

Health conscience people

Industry/Entity Type

Weight

Font styles to use
Sans Serif

Requirements
Must have
• -Size of bottle - 2" wide x 4" high
Nice to have
• *Lowers Hunger up to 50%
• *Decreases cravings or unhealthy foods up to 90%
• *Enhances Weight Loss
• " A Durovix a day keeps hunger away"

```html
<!DOCTYPE html>
<html lang="en">
<head>
<meta charset="utf-8">
<title>Kelvara Lithe — Label</title>
<link href="https://fonts.googleapis.com/css2?family=Playfair+Display:wght@700;900&family=Raleway:wght@300;400&family=Open+Sans:ital,wght@1,600;1,700&display=swap" rel="stylesheet">
<style>
  :root {
    --paper: #ffffff;
    --leaf: #4fa83a;
    --leaf-light: #7cc35a;
    --logo-ink: #5e5046;
    --navy: #0d2f6b;
    --teal: #1aa6c9;
    --sky: #9fdcec;
    --sky-pale: #d8f1f8;
    --spinach: #5f9a3c;
    --white: #ffffff;
  }
  * { margin: 0; padding: 0; box-sizing: border-box; }
  html, body { width: 951px; height: 1200px; overflow: hidden; background: var(--paper); }
  .label { position: relative; width: 951px; height: 1200px; background: var(--paper); }

  .product-name {
    position: absolute;
    top: 300px;
    writing-mode: vertical-rl;
    transform: rotate(180deg);
    font-family: "Playfair Display", serif;
    font-weight: 900;
    color: var(--leaf);
    white-space: nowrap;
    line-height: 1;
  }
  .product-name--first { left: 70px; font-size: 132px; }
  .product-name--second { left: 185px; font-size: 132px; top: 420px; }
  .product-sub {
    position: absolute;
    left: 318px;
    top: 440px;
    writing-mode: vertical-rl;
    transform: rotate(180deg);
    font-family: "Raleway", sans-serif;
    font-weight: 400;
    font-size: 30px;
    letter-spacing: 3px;
    color: var(--leaf-light);
    white-space: nowrap;
  }

  .brand {
    position: absolute;
    left: 420px;
    top: 220px;
    display: flex;
    align-items: center;
    gap: 14px;
    font-family: "Raleway", sans-serif;
    font-weight: 300;
    font-size: 72px;
    color: var(--logo-ink);
  }
  .brand__dot { width: 22px; height: 22px; border-radius: 50%; background: var(--leaf); }

  .rule {
    position: absolute;
    left: 370px;
    top: 338px;
    width: 560px;
    height: 8px;
    background: linear-gradient(90deg, var(--white), var(--teal) 45%, var(--navy));
  }

  .spinach-photo {
    position: absolute;
    left: 420px;
    top: 390px;
    width: 300px;
    height: 240px;
    border-radius: 48% 52% 45% 55%;
    background: radial-gradient(circle at 45% 40%, #8cc467, var(--spinach) 60%, #3f7a2a);
  }

  .claims {
    position: absolute;
    left: 370px;
    top: 690px;
    width: 581px;
    padding: 28px 30px 30px 24px;
    background: linear-gradient(90deg, var(--sky-pale), var(--sky) 40%, var(--teal));
    display: flex;
    flex-direction: column;
    gap: 18px;
  }
  .claim {
    display: flex;
    align-items: center;
    gap: 14px;
    padding: 14px 18px;
    background: linear-gradient(90deg, var(--teal), var(--navy));
    font-family: "Open Sans", sans-serif;
    font-style: italic;
    font-weight: 700;
    font-size: 25px;
    line-height: 1.2;
    color: var(--white);
  }
  .claim svg { flex: none; width: 30px; height: 30px; }

  .tagline {
    position: absolute;
    left: 370px;
    width: 581px;
    top: 1040px;
    text-align: center;
    font-family: "Open Sans", sans-serif;
    font-style: italic;
    font-weight: 700;
    font-size: 28px;
    color: var(--teal);
  }
</style>
</head>
<body>
<main class="label">
  <div class="product-name product-name--first">KELVARA</div>
  <div class="product-name product-name--second">LITHE</div>
  <div class="product-sub">W/ PURE DUROVIX</div>

  <div class="brand"><span>NuKelvara</span><span class="brand__dot"></span></div>
  <div class="rule"></div>

  <div class="spinach-photo" role="img" aria-label="Fresh spinach leaves"></div>

  <ul class="claims">
    <li class="claim">
      <svg viewBox="0 0 24 24"><path d="M3 13l6 6L21 6" fill="none" stroke="#ffffff" stroke-width="4" stroke-linecap="round" stroke-linejoin="round"/></svg>
      <span>Lowers Hunger up to 50%</span>
    </li>
    <li class="claim">
      <svg viewBox="0 0 24 24"><path d="M3 13l6 6L21 6" fill="none" stroke="#ffffff" stroke-width="4" stroke-linecap="round" stroke-linejoin="round"/></svg>
      <span>Decreases cravings or unhealthy foods up to 90%</span>
    </li>
    <li class="claim">
      <svg viewBox="0 0 24 24"><path d="M3 13l6 6L21 6" fill="none" stroke="#ffffff" stroke-width="4" stroke-linecap="round" stroke-linejoin="round"/></svg>
      <span>Enhances Weight Loss</span>
    </li>
  </ul>

  <p class="tagline">A Durovix a day keeps hunger away</p>
</main>
</body>
</html>
```